This is a book by, for and about bereaved parents and grandparents

I need a paperback size cover with front and back please...I have an example of a cover i had done myself and you will see a butterfly graphic within my Preface (My Story) which may be nice to include..or not.

Please feel free to explore your own psyche on this subject light and dark work accepted...love to see your concepts on this difficult subject.
thanks and good luck to you all!
Updates

Good Day Designer..I will post my current photo for the cover shortly and i cannot wait to see your great designs!

Apologies to you all for the delay in providing feedback ..I'm a little overwhelmed at the quality of your work and most likely will be adding a second and third place tonight when i finalize this project..thanks for your hard work and patience

thanks to all the designers for your heartfelt work on this project..it is so very personal to me and If i could afford it I'd pay you all ..do take care and thanks again for your submisions Marla .

https://www.quillnest.com/Lanterns-Along-the-Quiet-Shore-4837201956310482/?epa=SEARCH_BOX

Target Market(s)

Family of children who have died before their time especially those who've left parents and grandparents to grieve their loss of all ages.

Industry/Entity Type

Writer

Font styles to use
Serif
Sans Serif
Decorative
Script

Colors

Designer to choose colors to be used in the design.

Requirements
Must have
• feeling of loss and renewal important to end in hope and faith for future despite the years and months and days of pure agony
• my pic
• my name to be seen clearly on front of paperback
Nice to have
• maybe my butterfly graphic if it works with your concept?
• I would appreciate it if you read my Preface it 23 pages but I hope it will provide insight into the contents of the book thanks for your time and patience
Should not have
• Gravestones religous icons
• such as crosses etc

```html
<!DOCTYPE html>
<html lang="en">
<head>
<meta charset="utf-8">
<title>Lanterns Along the Quiet Shore – Cover</title>
<link href="https://fonts.googleapis.com/css2?family=Bebas+Neue&family=Arimo:wght@400;700&display=swap" rel="stylesheet">
<style>
  :root{
    --stage:#5f5f5f;
    --ink:#111111;
    --accent-red:#e0202a;
    --body-ink:#1e1e1e;
    --art-warm:#b58a5c;
    --art-pale:#e8e3dc;
    --art-mint:#bfe3d3;
    --art-rose:#e6c6c8;
    --art-dark:#3b2a22;
    --wing-blue:#1aa7f0;
    --wing-deep:#0b4fa8;
    --panel-veil:rgba(255,255,255,.42);
  }
  *{box-sizing:border-box;margin:0;padding:0}
  html,body{width:1200px;height:1070px;overflow:hidden;background:var(--stage)}
  .spread{position:absolute;left:50px;top:135px;width:1100px;height:800px;display:flex;gap:20px}
  .cover{position:relative;width:540px;height:800px;overflow:hidden;box-shadow:0 10px 30px rgba(0,0,0,.35)}
  .cover-art{position:absolute;inset:0;
    background:
      radial-gradient(ellipse 55% 35% at 40% 12%, var(--art-dark) 0%, rgba(59,42,34,0) 70%),
      radial-gradient(ellipse 60% 30% at 35% 60%, var(--art-mint) 0%, rgba(191,227,211,0) 70%),
      radial-gradient(ellipse 50% 30% at 70% 75%, var(--art-rose) 0%, rgba(230,198,200,0) 70%),
      linear-gradient(160deg, var(--art-warm) 0%, var(--art-pale) 35%, var(--art-pale) 65%, var(--art-warm) 100%);}
  .butterfly{position:absolute;border-radius:40% 40% 50% 50%;
    background:radial-gradient(circle at 50% 45%, var(--wing-blue), var(--wing-deep));}
  .butterfly--large{left:315px;top:110px;width:140px;height:120px}
  .butterfly--small{left:280px;top:470px;width:110px;height:55px;opacity:.75}

  .title{position:absolute;left:0;right:0;top:300px;text-align:center;color:var(--ink);line-height:.95}
  .title .big{font-family:'Bebas Neue',sans-serif;font-size:82px;letter-spacing:0}
  .title .small{font-family:'Arimo',sans-serif;font-size:52px}
  .title .line{display:block}
  .subtitle{position:absolute;left:0;right:0;top:585px;text-align:center;font-family:'Arimo',sans-serif;font-size:27px;line-height:1.3;color:var(--ink)}
  .byline{position:absolute;left:0;right:0;top:675px;text-align:center;font-family:'Arimo',sans-serif;color:var(--ink)}
  .byline .by{display:block;font-size:26px}
  .byline .author{display:block;font-size:26px;letter-spacing:1.5px;margin-top:4px}

  .back-panel{position:absolute;left:18px;top:18px;right:18px;bottom:18px;background:var(--panel-veil)}
  .back-text{position:absolute;left:28px;top:90px;width:470px;font-family:'Arimo',sans-serif;font-size:13.5px;line-height:1.3;color:var(--body-ink)}
  .back-text p{margin-bottom:14px}
  .about{position:absolute;left:28px;top:560px;right:28px;display:flex;gap:20px}
  .author-photo{flex:none;width:105px;height:140px;margin-top:10px;background:linear-gradient(180deg,#8a5a3c,#e9b8a4 55%,#d8307a)}
  .about-body h2{font-family:'Arimo',sans-serif;font-weight:400;font-size:26px;color:var(--accent-red);margin-bottom:10px}
  .about-body p{font-family:'Arimo',sans-serif;font-size:13px;line-height:1.3;color:var(--body-ink)}
</style>
</head>
<body>
<main class="spread">
  <section class="cover cover--back">
    <div class="cover-art" role="img" aria-label="Painterly textured background in warm browns and pale pastels"></div>
    <div class="back-panel"></div>
    <div class="back-text">
      <p>My amazing first born son, Rowan has held my hand and my heart and has shown incredible strength and fortitude after losing his precious only sister and nephew.<br>He was too young to have memories of his little brother, Elliot but I do remember it had at the time caused him great distress.</p>
      <p>His loving wife, Greta was there for me through some of my most difficult hours in South Africa on the night we laid Tessa and Milo to rest at their funeral and has continued to be there throughout this journey as she, herself grieves this loss.<br>And how precious is the gift of their sweet daughter and the gratitude I feel for the joy she’s brought into our lives.<br>She is the beacon that guides us forward to the future.</p>
      <p>My amazing first born son, Rowan has held my hand and my heart and has shown incredible strength and fortitude after losing his precious only sister and nephew.<br>He was too young to have memories of his little brother, Elliot but I do remember it had at the time caused him great distress.</p>
    </div>
    <div class="about">
      <div class="author-photo" role="img" aria-label="Portrait photo of the author"></div>
      <div class="about-body">
        <h2>ABOUT THE AUTHOR</h2>
        <p>I need a paperback size cover with front and back please...I have an example of a cover I had done myself and you will see a butterfly graphic within my Preface (My Story) which may be nice to include..or not. Please feel free to explore your own psyche on this subject light and dark work accepted...love to see your concepts on this difficult subject.</p>
      </div>
    </div>
  </section>

  <section class="cover cover--front">
    <div class="cover-art" role="img" aria-label="Painterly textured artwork of a grieving face in soft pastel and brown tones"></div>
    <div class="butterfly butterfly--large" role="img" aria-label="Bright blue butterfly illustration"></div>
    <div class="butterfly butterfly--small" role="img" aria-label="Small translucent blue butterfly illustration"></div>
    <h1 class="title">
      <span class="line"><span class="big">LANTERNS</span> <span class="small">along</span></span>
      <span class="line"><span class="small">the</span></span>
      <span class="line"><span class="big">QUIET SHORE</span></span>
    </h1>
    <p class="subtitle">Grieving the death of a child<br>in an open and healthy way</p>
    <p class="byline"><span class="by">by</span><span class="author">MARLA WHITCOMBE HALE</span></p>
  </section>
</main>
</body>
</html>
```